iOS App Design Project for Pebble Tasks

We are looking for a redesign of the UI for our app, Pebble Tasks. The app is a to-do list type app with 4 screens, and we already have a UI for it but we would like a nicer looking one that has a better colour scheme and is more intuitive.

We would like something that is a real treat to look at, and that users really want to use. Essentially what we want is the nicest and most simple design possible, as the current UI we have is not very user friendly.

The app is already on the market and is free so if you have an iOS device you can download it and take a look at it, and we have also included screenshots of the app.
Updates

Project Deadline Extended
Reason: I am updating the design brief and will also guarantee the payment.

Target Market(s)

Mobile users looking for simplicity

Requirements
Must have
• - Very visually pleasing
- Simple layout with minimal clutter
- Icons and buttons that explain what they do
Should not have
• Any features that detract from the simplicity of the app are not wanted.

```html
<!DOCTYPE html>
<html lang="en">
<head>
<meta charset="utf-8">
<title>Pebble Tasks – Notes</title>
<link href="https://fonts.googleapis.com/css2?family=Raleway:wght@100;200&family=Roboto:wght@400;700&display=swap" rel="stylesheet">
<style>
  :root {
    --status-top: #f4f5f6;
    --status-bottom: #d9dcdf;
    --header-bg: #cfd6e3;
    --header-text: #ffffff;
    --paper: #f8f7ef;
    --rule: #c9dce4;
    --margin-red: #eaa3a3;
    --tab-top: #6c7c92;
    --tab-bottom: #2d3848;
    --tab-active: rgba(255,255,255,0.22);
    --tab-icon: #e9edf3;
    --ink: #1b1b1b;
    --signal-blue: #2a7fd6;
    --save-red: #d6474d;
    --warn-green: #a8c24a;
    --info-green: #3eab47;
  }
  * { box-sizing: border-box; margin: 0; padding: 0; }
  html, body { width: 769px; height: 1200px; overflow: hidden; }
  body { background: var(--paper); font-family: "Roboto", Arial, sans-serif; position: relative; }

  .status-bar {
    position: absolute; top: 0; left: 0; width: 769px; height: 42px;
    background: linear-gradient(var(--status-top), var(--status-bottom));
    display: flex; align-items: center; justify-content: space-between;
    padding: 0 14px; color: var(--ink); font-weight: 700; font-size: 28px;
  }
  .status-left, .status-right { display: flex; align-items: center; gap: 10px; }
  .network { color: var(--signal-blue); }
  .status-time { position: absolute; left: 0; right: 0; text-align: center; pointer-events: none; }

  .app-header {
    position: absolute; top: 42px; left: 0; width: 769px; height: 160px;
    background: var(--header-bg);
  }
  .app-title {
    position: absolute; left: 14px; top: 14px;
    font-family: "Raleway", Arial, sans-serif; font-weight: 100;
    font-size: 80px; color: var(--header-text); letter-spacing: -1px;
    text-shadow: 0 0 1px #9aa4b4;
  }
  .header-actions { position: absolute; right: 36px; top: 24px; display: flex; gap: 30px; }
  .torn-edge { position: absolute; left: 0; bottom: -1px; width: 769px; height: 30px; }

  .paper {
    position: absolute; top: 202px; left: 0; width: 769px; height: 878px;
    background-color: var(--paper);
    background-image: repeating-linear-gradient(to bottom, transparent 0 40px, var(--rule) 40px 42px);
    background-position: 0 36px;
  }
  .margin-line { position: absolute; top: 0; bottom: 0; width: 2px; background: var(--margin-red); }
  .margin-line.outer { left: 68px; }
  .margin-line.inner { left: 82px; }

  .tab-bar {
    position: absolute; bottom: 0; left: 0; width: 769px; height: 120px;
    background: linear-gradient(var(--tab-top), var(--tab-bottom));
    display: flex; justify-content: space-around; align-items: center; padding: 0 10px;
  }
  .tab {
    width: 180px; height: 106px; display: flex; flex-direction: column;
    align-items: center; justify-content: center; gap: 4px;
    color: var(--tab-icon); font-size: 22px; font-weight: 700;
    border-radius: 4px;
  }
  .tab.is-active { background: var(--tab-active); box-shadow: inset 0 0 0 2px rgba(255,255,255,0.15); }
</style>
</head>
<body>
  <div class="status-bar">
    <div class="status-left">
      <svg width="46" height="24" viewBox="0 0 46 24" aria-hidden="true">
        <g fill="var(--signal-blue)">
          <rect x="0" y="16" width="6" height="8"/><rect x="9" y="12" width="6" height="12"/>
          <rect x="18" y="8" width="6" height="16"/><rect x="27" y="4" width="6" height="20"/>
          <rect x="36" y="0" width="6" height="24"/>
        </g>
      </svg>
      <span class="carrier">Orbit</span>
      <span class="network">3G</span>
    </div>
    <span class="status-time">12:00 PM</span>
    <div class="status-right">
      <svg width="26" height="26" viewBox="0 0 26 26" aria-hidden="true">
        <circle cx="13" cy="13" r="11" fill="#7b7f86"/>
        <path d="M13 13 V5 A8 8 0 0 1 21 13 Z" fill="#e6e8ea"/>
      </svg>
      <span>65%</span>
      <svg width="54" height="26" viewBox="0 0 54 26" aria-hidden="true">
        <rect x="1" y="2" width="46" height="22" rx="3" fill="none" stroke="#333" stroke-width="2"/>
        <rect x="48" y="8" width="4" height="10" fill="#333"/>
        <rect x="4" y="5" width="30" height="16" fill="#5ac43c"/>
      </svg>
    </div>
  </div>

  <header class="app-header">
    <h1 class="app-title">NOTES</h1>
    <div class="header-actions">
      <svg class="icon-save" width="66" height="66" viewBox="0 0 66 66" aria-label="Save">
        <g fill="none" stroke="var(--save-red)" stroke-width="3">
          <path d="M4 4 H54 L62 12 V62 H4 Z"/>
          <rect x="14" y="4" width="32" height="20"/>
          <rect x="16" y="36" width="34" height="26"/>
          <rect x="20" y="44" width="10" height="10"/>
        </g>
      </svg>
      <svg class="icon-warning" width="70" height="66" viewBox="0 0 70 66" aria-label="Report">
        <path d="M35 4 L66 62 H4 Z" fill="none" stroke="var(--warn-green)" stroke-width="3"/>
        <rect x="33" y="22" width="4" height="24" fill="var(--warn-green)"/>
        <rect x="33" y="51" width="4" height="5" fill="var(--warn-green)"/>
      </svg>
      <svg class="icon-info" width="66" height="66" viewBox="0 0 66 66" aria-label="Info">
        <circle cx="33" cy="33" r="30" fill="none" stroke="var(--info-green)" stroke-width="3"/>
        <circle cx="35" cy="16" r="5" fill="var(--info-green)"/>
        <path d="M26 28 H38 L32 50 H40" fill="none" stroke="var(--info-green)" stroke-width="6" stroke-linejoin="round"/>
      </svg>
    </div>
    <svg class="torn-edge" viewBox="0 0 769 30" preserveAspectRatio="none" aria-hidden="true">
      <path fill="var(--paper)" d="M0 12 L30 10 L60 14 L95 9 L130 13 L170 8 L210 14 L250 11 L290 15 L330 9 L370 13 L410 10 L450 16 L490 11 L530 14 L570 9 L610 13 L650 10 L690 15 L730 11 L769 13 V30 H0 Z"/>
      <path fill="none" stroke="#b5bfcc" stroke-width="2" d="M0 12 L30 10 L60 14 L95 9 L130 13 L170 8 L210 14 L250 11 L290 15 L330 9 L370 13 L410 10 L450 16 L490 11 L530 14 L570 9 L610 13 L650 10 L690 15 L730 11 L769 13"/>
    </svg>
  </header>

  <main class="paper" aria-label="Note page">
    <div class="margin-line outer"></div>
    <div class="margin-line inner"></div>
  </main>

  <nav class="tab-bar">
    <div class="tab">
      <svg width="70" height="60" viewBox="0 0 70 60" aria-hidden="true">
        <g fill="var(--tab-icon)">
          <circle cx="7" cy="8" r="4"/><rect x="16" y="5" width="52" height="6"/>
          <circle cx="7" cy="23" r="4"/><rect x="16" y="20" width="52" height="6"/>
          <circle cx="7" cy="38" r="4"/><rect x="16" y="35" width="52" height="6"/>
          <circle cx="7" cy="53" r="4"/><rect x="16" y="50" width="52" height="6"/>
        </g>
      </svg>
      <span>List</span>
    </div>
    <div class="tab">
      <svg width="70" height="60" viewBox="0 0 70 60" aria-hidden="true">
        <rect x="6" y="12" width="46" height="44" fill="none" stroke="var(--tab-icon)" stroke-width="5"/>
        <path d="M16 32 L28 46 L62 4" fill="none" stroke="var(--tab-icon)" stroke-width="8"/>
      </svg>
      <span>Task</span>
    </div>
    <div class="tab is-active">
      <svg width="70" height="60" viewBox="0 0 70 60" aria-hidden="true">
        <g fill="none" stroke="var(--tab-icon)" stroke-width="4">
          <rect x="6" y="8" width="46" height="48"/>
          <path d="M12 2 V12 M22 2 V12 M32 2 V12 M42 2 V12"/>
          <path d="M36 52 L60 24 L66 30 L42 58 L34 60 Z"/>
        </g>
      </svg>
      <span>Note</span>
    </div>
    <div class="tab">
      <svg width="60" height="60" viewBox="0 0 60 60" aria-hidden="true">
        <circle cx="30" cy="30" r="28" fill="var(--tab-icon)"/>
        <path d="M30 14 V46 M14 30 H46" stroke="#3a4658" stroke-width="8"/>
      </svg>
      <span>More</span>
    </div>
  </nav>
</body>
</html>
```